Harbor Fieldworks (Business Card Design)

Need business cards designed. Something modern, chic, and sleek. Mabye the back of the card should be the navy blue that is in the logo and then just the logo on the back.

Target Market(s)

Those in the hotel, office, and renovation industry

Contact Information for Business Card

1. Logo 2. Dorian Velasko 3. CEO/Founder 4. Phone: (833) HarbFld / (833) 427-2353 5. Email: dorian@theharborfieldworks.com 6. Website: www.theharborfieldworks.com

Font styles to use
Other font styles liked:
• Look at the logo font and base the font for everything else off of that.

Colors
0054AA
0677BA
7BADD7
CADEEF
E8F1F8

Requirements
Must have
• Colors that are associated in the logo
Nice to have
• Sleek modern clean and chic design.

```html
<!DOCTYPE html>
<html lang="en">
<head>
<meta charset="utf-8">
<title>Harbor Fieldworks — Business Card</title>
<link rel="stylesheet" href="https://fonts.googleapis.com/css2?family=Montserrat:wght@400;500;700;800&display=swap">
<style>
  :root {
    --backdrop: #2a2a2c;
    --navy: #0c1a44;
    --gold: #c9a04a;
    --white: #ffffff;
    --ink: #1c1c24;
  }
  * { margin: 0; padding: 0; box-sizing: border-box; }
  html, body {
    width: 1200px;
    height: 875px;
    overflow: hidden;
    background: var(--backdrop);
    font-family: "Montserrat", sans-serif;
  }
  .canvas {
    position: relative;
    width: 1200px;
    height: 875px;
  }
  .card {
    position: absolute;
    top: 282px;
    width: 540px;
    height: 310px;
    border-radius: 22px;
    overflow: hidden;
  }
  .card-front { left: 40px; background: var(--white); }
  .card-back { left: 620px; background: var(--navy); }

  /* front: brand name block */
  .front-brand {
    position: absolute;
    right: 38px;
    top: 44px;
    display: flex;
    align-items: flex-start;
    gap: 12px;
  }
  .brand-square {
    width: 16px;
    height: 16px;
    background: var(--gold);
    flex: none;
    margin-top: 8px;
  }
  .front-brand .brand-name {
    font-weight: 800;
    font-size: 30px;
    line-height: 1.1;
    color: var(--navy);
    text-transform: uppercase;
    letter-spacing: 0.04em;
    text-align: right;
  }

  /* front: person details */
  .person {
    position: absolute;
    left: 38px;
    bottom: 34px;
  }
  .person-name {
    font-weight: 800;
    font-size: 30px;
    color: var(--navy);
    line-height: 1;
  }
  .person-title {
    font-weight: 500;
    font-size: 17px;
    color: var(--gold);
    margin-top: 6px;
  }
  .rule {
    width: 44px;
    height: 2px;
    background: var(--navy);
    margin: 10px 0 12px;
  }
  .contact-list { list-style: none; }
  .contact-list li {
    display: flex;
    align-items: center;
    gap: 10px;
    font-size: 13.5px;
    font-weight: 400;
    color: var(--ink);
    line-height: 1.55;
  }
  .contact-list svg {
    width: 13px;
    height: 13px;
    flex: none;
    fill: var(--gold);
  }

  /* back */
  .back-brand {
    position: absolute;
    inset: 0;
    display: flex;
    align-items: center;
    justify-content: center;
    gap: 16px;
  }
  .back-brand .brand-square { margin-top: 0; }
  .back-brand .brand-name {
    font-weight: 700;
    font-size: 34px;
    letter-spacing: 0.08em;
    text-transform: uppercase;
    color: var(--white);
  }
</style>
</head>
<body>
<main class="canvas">

  <section class="card card-front" aria-label="Card front">
    <div class="front-brand">
      <p class="brand-name">Harbor<br>Fieldworks</p>
      <span class="brand-square"></span>
    </div>

    <div class="person">
      <h1 class="person-name">Dorian Velasko</h1>
      <p class="person-title">CEO/Founder</p>
      <div class="rule"></div>
      <ul class="contact-list">
        <li>
          <svg viewBox="0 0 24 24" aria-hidden="true"><path d="M6.6 10.8a15.1 15.1 0 0 0 6.6 6.6l2.2-2.2a1 1 0 0 1 1-.25 11.4 11.4 0 0 0 3.6.57 1 1 0 0 1 1 1V20a1 1 0 0 1-1 1A17 17 0 0 1 3 4a1 1 0 0 1 1-1h3.5a1 1 0 0 1 1 1c0 1.25.2 2.45.57 3.6a1 1 0 0 1-.25 1z"/></svg>
          (833) HarbFld
        </li>
        <li>
          <svg viewBox="0 0 24 24" aria-hidden="true"><path d="M6.6 10.8a15.1 15.1 0 0 0 6.6 6.6l2.2-2.2a1 1 0 0 1 1-.25 11.4 11.4 0 0 0 3.6.57 1 1 0 0 1 1 1V20a1 1 0 0 1-1 1A17 17 0 0 1 3 4a1 1 0 0 1 1-1h3.5a1 1 0 0 1 1 1c0 1.25.2 2.45.57 3.6a1 1 0 0 1-.25 1z"/></svg>
          (833) 427-2353
        </li>
        <li>
          <svg viewBox="0 0 24 24" aria-hidden="true"><path d="M2 5h20v14H2zm2 2v.5l8 5 8-5V7zm0 2.9V17h16V9.9l-8 5z"/></svg>
          dorian@theharborfieldworks.com
        </li>
        <li>
          <svg viewBox="0 0 24 24" aria-hidden="true"><path d="M12 2a10 10 0 1 0 0 20 10 10 0 0 0 0-20zm6.9 6h-3a15.7 15.7 0 0 0-1.4-3.6A8 8 0 0 1 18.9 8zM12 4c.8 1.2 1.5 2.5 1.9 4h-3.8c.4-1.5 1.1-2.8 1.9-4zM4.3 14a8 8 0 0 1 0-4h3.4a16.5 16.5 0 0 0 0 4zm.8 2h3a15.7 15.7 0 0 0 1.4 3.6A8 8 0 0 1 5.1 16zm3-8h-3a8 8 0 0 1 4.4-3.6A15.7 15.7 0 0 0 8.1 8zM12 20c-.8-1.2-1.5-2.5-1.9-4h3.8c-.4 1.5-1.1 2.8-1.9 4zm2.3-6H9.7a14.7 14.7 0 0 1 0-4h4.6a14.7 14.7 0 0 1 0 4zm.2 5.6a15.7 15.7 0 0 0 1.4-3.6h3a8 8 0 0 1-4.4 3.6zm1.8-5.6a16.5 16.5 0 0 0 0-4h3.4a8 8 0 0 1 0 4z"/></svg>
          www.theharborfieldworks.com
        </li>
      </ul>
    </div>
  </section>

  <section class="card card-back" aria-label="Card back">
    <div class="back-brand">
      <span class="brand-square"></span>
      <p class="brand-name">Harbor Fieldworks</p>
    </div>
  </section>

</main>
</body>
</html>
```